Postcard Design

Nonprofit agency needs quick turnaround postcard design to help boost attendance at a fundraiser to support a program that helps find homes for children in foster care.

The front should just be the artwork. The back should be the information in an easy to read, attractive layout. The logo and the elevation drawing need to be integrated into the layout.

Industry/Entity Type

It Support

```html
<!DOCTYPE html>
<html lang="en">
<head>
<meta charset="utf-8">
<title>House Party Postcard</title>
<link href="https://fonts.googleapis.com/css2?family=Arimo:wght@400;700&display=swap" rel="stylesheet">
<style>
:root{
  --bg:#3f4045;
  --card:#ffffff;
  --ink:#111111;
  --green:#1e8a3c;
  --leaf:#6db33f;
  --line:#111111;
}
*{margin:0;padding:0;box-sizing:border-box}
html,body{width:1200px;height:1000px;overflow:hidden;background:var(--bg)}
body{position:relative;font-family:"Arimo",Arial,sans-serif;color:var(--ink)}
.card{position:absolute;background:var(--card)}
.card-front{left:270px;top:52px;width:853px;height:608px;overflow:hidden}
.front-artwork{position:absolute;inset:0;width:100%;height:100%}
.card-back{left:50px;top:303px;width:851px;height:609px}
.headline{position:absolute;left:38px;top:28px;font-size:18.5px;font-weight:700;color:var(--green);letter-spacing:-.1px}
.intro{position:absolute;left:38px;top:56px;width:626px;font-size:11.3px;line-height:16.4px;text-align:justify}
.intro p{margin-bottom:2px}
.galleries{margin-top:15px;font-weight:700;font-size:11.3px;line-height:16.4px}
.postage{position:absolute;left:700px;top:29px;width:123px;height:123px;border:1.5px solid var(--line);display:flex;align-items:center;justify-content:center;font-size:19px}
.elevation{position:absolute;left:38px;top:247px;width:276px;height:174px}
.address-area{position:absolute;left:335px;top:275px;width:456px;height:259px;border:1.5px solid var(--line);display:flex;align-items:center;justify-content:center;font-size:19px}
.closing{position:absolute;left:38px;top:437px;width:270px;font-size:11.3px;line-height:16.4px;text-align:justify}
.tickets{position:absolute;left:38px;top:514px;font-size:11px;font-weight:700;line-height:16px}
.tickets .big{font-size:13.5px}
.agency{position:absolute;left:222px;top:506px;width:90px;text-align:center}
.agency-dot{display:block;width:22px;height:22px;border-radius:50%;background:var(--leaf);margin:0 auto 6px}
.agency-name{font-size:11px;line-height:13px;color:var(--leaf);font-weight:400}
</style>
</head>
<body>

<section class="card card-front">
  <svg class="front-artwork" role="img" aria-label="Front artwork: quilt of patterned scalloped fabric shapes in green, purple, yellow, black, blue and orange" viewBox="0 0 853 608" preserveAspectRatio="none">
    <defs>
      <linearGradient id="quiltTone" x1="0" y1="0" x2="1" y2="1">
        <stop offset="0" stop-color="#5d7a3a"/>
        <stop offset=".3" stop-color="#6b5a66"/>
        <stop offset=".5" stop-color="#e7a93a"/>
        <stop offset=".7" stop-color="#3a3536"/>
        <stop offset="1" stop-color="#8aa7d6"/>
      </linearGradient>
    </defs>
    <rect width="853" height="608" fill="#f1f1f1"/>
    <rect x="0" y="0" width="853" height="608" fill="url(#quiltTone)" opacity=".85"/>
  </svg>
</section>

<section class="card card-back">
  <h1 class="headline">Nashville’s most exciting Party is almost here!</h1>
  <div class="intro">
    <p>There are limited number of tickets left for Harbor Family Alliance’ House Party, October 30th at 6PM. This is a preview of the spectacular renovation of the iconic modern Belle Meade residence of Dr. and Mrs. Harold Whitcomb, now the home of Marco Bellandi and Peter Ashcroft of Ashby &amp; Lorne. The event will benefit the Bridging Kids program at HFA, which helps prepare foster children for adoption.</p>
    <p>The evening will feature an incredible selection of modern art from established and emerging artists personally chosen by the home’s designers/owners and curated by Eleanor M. Vance, of The Riverside Art Museum, Louisville. Galleries featured include the following:</p>
    <div class="galleries">
      The Harlan Reed Gallery, Nashville/Memphis<br>
      The Clara Dunn Gallery, Nashville<br>
      Mercer Projects, New York
    </div>
  </div>

  <div class="postage">Postage</div>

  <svg class="elevation" role="img" aria-label="Elevation drawing of the modern residence with lawn and trees" viewBox="0 0 276 174" preserveAspectRatio="none">
    <defs>
      <linearGradient id="elevTone" x1="0" y1="0" x2="0" y2="1">
        <stop offset="0" stop-color="#2f9a44"/>
        <stop offset=".4" stop-color="#e9ecef"/>
        <stop offset=".65" stop-color="#c2de3c"/>
        <stop offset="1" stop-color="#a9cf2e"/>
      </linearGradient>
    </defs>
    <rect width="276" height="174" fill="url(#elevTone)"/>
  </svg>

  <div class="address-area">Address / OCR Read Area</div>

  <p class="closing">Both the home and the artwork are a must-see. A portion of the artwork sales on the evening of the event will benefit Harbor Family Alliance. Tickets will sell out and must be purchased in advance.</p>

  <div class="tickets">
    To purchase tickets, please visit<br>
    <span class="big">www.hfanashville.org</span><br>
    or call Laura Kemper Ross<br>
    at <span class="big">615-555-0142.</span>
  </div>

  <div class="agency">
    <span class="agency-dot"></span>
    <span class="agency-name">Harbor Family<br>Alliance</span>
  </div>
</section>

</body>
</html>
```